Business Card Design Project

KB Consulting Associates is a management consulting business with C-suite (CEO/CFO etc) target clients. Logo selected is blue with simple/serious typefaces.

Target Market(s)

CEOs and CFOs of large corporates

Industry/Entity Type

Management Consulting

Font styles to use
Serif

Colors
3276b5

Requirements
Must have
• Tag line: Building successful collaborations (use different font)
Address: 427 Fernvale Crescent #03-22 Singapore 519337
Telephone: +65 8372 4096
Email: kbloh@postnest42.com

```html
<!DOCTYPE html>
<html lang="en">
<head>
<meta charset="utf-8">
<title>KB Consulting Associates — Business Card</title>
<link rel="stylesheet" href="https://fonts.googleapis.com/css2?family=Questrial&family=Tinos:ital,wght@0,700;1,400&family=Sacramento&display=swap">
<style>
  :root {
    --brand-blue: #0a83c5;
    --band-grey: #c4c4c4;
    --ink: #111111;
    --tagline-grey: #9a9a9a;
    --card-edge: #222222;
    --paper: #ffffff;
  }
  html, body {
    margin: 0;
    padding: 0;
    width: 1200px;
    height: 1000px;
    overflow: hidden;
    background: var(--paper);
  }
  .canvas {
    position: relative;
    width: 1200px;
    height: 1000px;
  }
  .card {
    position: absolute;
    top: 323px;
    width: 574px;
    height: 355px;
    border: 1px solid var(--card-edge);
    border-radius: 22px;
    box-sizing: border-box;
    overflow: hidden;
    background: var(--paper);
  }
  .card--front { left: 16px; }
  .card--back { left: 609px; }

  .band {
    position: absolute;
    top: 146px;
    height: 60px;
    display: flex;
    align-items: center;
  }
  .band--blue { background: var(--brand-blue); }
  .band--grey { background: var(--band-grey); }

  .front-brand {
    left: 0;
    width: 214px;
    justify-content: center;
  }
  .brand-name {
    font-family: "Questrial", sans-serif;
    font-weight: 400;
    color: #ffffff;
    font-size: 15px;
    white-space: nowrap;
  }
  .person-name {
    position: absolute;
    left: 223px;
    top: 165px;
    font-family: "Questrial", sans-serif;
    font-size: 18px;
    letter-spacing: 2px;
    color: var(--ink);
  }
  .contact {
    right: 0;
    width: 191px;
    flex-direction: column;
    align-items: flex-end;
    justify-content: center;
    padding-right: 20px;
    box-sizing: border-box;
    font-family: "Tinos", serif;
    color: var(--ink);
    line-height: 1.1;
  }
  .contact__phone { font-weight: 700; font-size: 17px; }
  .contact__email { font-style: italic; font-size: 16px; }

  .address {
    left: 0;
    width: 481px;
    padding-left: 15px;
    box-sizing: border-box;
  }
  .address__text {
    font-family: "Questrial", sans-serif;
    font-variant: small-caps;
    color: #ffffff;
    font-size: 16px;
    letter-spacing: 0.9px;
    white-space: nowrap;
  }
  .back-brand {
    right: 0;
    width: 92px;
    justify-content: center;
  }
  .back-brand__name {
    font-family: "Questrial", sans-serif;
    font-weight: 400;
    color: var(--brand-blue);
    font-size: 9px;
    line-height: 1.15;
    text-align: center;
  }
  .tagline {
    position: absolute;
    right: 94px;
    top: 210px;
    font-family: "Sacramento", cursive;
    font-size: 23px;
    color: var(--tagline-grey);
    white-space: nowrap;
  }
</style>
</head>
<body>
<main class="canvas">
  <section class="card card--front" aria-label="Card front">
    <div class="band band--blue front-brand">
      <span class="brand-name">KB Consulting Associates</span>
    </div>
    <div class="person-name">KBLOH</div>
    <div class="band band--grey contact">
      <span class="contact__phone">+65 8372 4096</span>
      <span class="contact__email">kbloh@postnest42.com</span>
    </div>
  </section>

  <section class="card card--back" aria-label="Card back">
    <div class="band band--blue address">
      <span class="address__text">427 Fernvale Crescent #03-22 Singapore 519337</span>
    </div>
    <div class="band band--grey back-brand">
      <span class="back-brand__name">KB Consulting<br>Associates</span>
    </div>
    <div class="tagline">Building successful collaborations</div>
  </section>
</main>
</body>
</html>
```